Travel Company is looking for a STAND OUT Business Card

I need a unique Business Card that will truly stand out. Nothing too busy. Simple is good, right? Not looking for a standard design either. No cookie cutter layout. We are a Travel Company that works more with Companies than Travelers. I had an idea to focus and emphasis on the 2 logo a bit more. This is not necessary, however thought it would look interesting. I am just looking for something interesting and a bit different. Does't have to completely off the wall crazy, just not your run of the mill business card.

Target Market(s)

Hoteliers, Resort Management, Call Centers, Executives, Travelers, Families, Businesses

Industry/Entity Type

Hospitality

Contact Information for Business Card

President/CEO - Marcus T Bellamy (title not necessary if design doesn't allow for it)
contact - (407) 555-0186
email - mbellamy@wayfarenow.example
address - 4812 Quillmore Ave #164
Orlando, FL 32804
website - www.wayfarenow.example

Font styles to use
Serif
Other font styles liked:
• Avenir Next LT Pro BOLD

Requirements
Must have
• simple look and design. Unique design
Nice to have
• I attached the 2 logo separate from the main logo. This can be used separately from the Main Logo, together with the main logo or as main logo. I included the logo font. Use it or not, designers choice.
Should not have
• cookie cutter design. Little use of red other than the logo

```html
<!DOCTYPE html>
<html lang="en">
<head>
<meta charset="utf-8">
<title>Wayfare Now – Business Card</title>
<link href="https://fonts.googleapis.com/css2?family=Nunito+Sans:wght@400;600;800&display=swap" rel="stylesheet">
<style>
  :root {
    --bg: #d4d4d4;
    --red: #ee1c25;
    --ink: #231f20;
    --ink-soft: #2c2829;
    --paper: #ffffff;
    --muted: #e6e6e6;
  }
  * { box-sizing: border-box; margin: 0; padding: 0; }
  html, body { width: 1200px; height: 800px; overflow: hidden; }
  body {
    background: var(--bg);
    font-family: "Nunito Sans", "Avenir Next", sans-serif;
    display: flex;
    align-items: center;
    justify-content: center;
    gap: 40px;
  }
  .card {
    width: 520px;
    height: 297px;
    position: relative;
    overflow: hidden;
    box-shadow: 0 10px 24px rgba(0,0,0,.18);
  }

  /* Front side */
  .card--front { background: var(--ink); }
  .frame-top {
    position: absolute; left: 0; top: 0;
    width: 290px; height: 18px;
    background: var(--red);
  }
  .frame-left {
    position: absolute; left: 0; top: 0;
    width: 18px; height: 212px;
    background: var(--red);
  }
  .frame-inner {
    position: absolute; left: 18px; top: 18px;
    width: 272px; height: 194px;
    border-left: 0;
  }
  .watermark-ring {
    position: absolute; left: 185px; top: 55px;
    width: 190px; height: 190px;
    border-radius: 50%;
    border: 22px solid var(--ink-soft);
  }
  .identity {
    position: absolute; left: 44px; top: 44px;
    padding-left: 12px;
    border-left: 2px solid var(--red);
  }
  .identity__name {
    color: var(--paper);
    font-weight: 800;
    font-size: 19px;
    line-height: 1.1;
  }
  .identity__title {
    color: var(--red);
    font-weight: 600;
    font-size: 12px;
    margin-top: 2px;
  }
  .contacts {
    position: absolute; right: 30px; top: 130px;
    list-style: none;
    text-align: right;
  }
  .contact {
    display: flex;
    justify-content: flex-end;
    align-items: center;
    gap: 8px;
    color: var(--muted);
    font-size: 12.5px;
    line-height: 1.25;
    margin-bottom: 8px;
  }
  .contact__icon { width: 14px; height: 14px; flex: none; }
  .contact__bar {
    width: 2px; align-self: stretch; min-height: 18px;
    background: var(--red);
    flex: none;
  }

  /* Back side */
  .card--back {
    background: var(--red);
    display: flex;
    align-items: center;
    justify-content: center;
    gap: 12px;
  }
  .brand__dot {
    width: 34px; height: 34px; border-radius: 50%;
    background: var(--paper);
  }
  .brand__name {
    color: var(--paper);
    font-weight: 800;
    font-size: 42px;
    letter-spacing: -0.5px;
  }
</style>
</head>
<body>
  <section class="card card--front" aria-label="Business card front">
    <div class="frame-top"></div>
    <div class="frame-left"></div>
    <div class="watermark-ring" aria-hidden="true"></div>
    <div class="identity">
      <p class="identity__name">Marcus T Bellamy</p>
      <p class="identity__title">President/CEO</p>
    </div>
    <ul class="contacts">
      <li class="contact">
        <span>(407) 555-0186</span>
        <svg class="contact__icon" viewBox="0 0 14 14" fill="none" stroke="#ee1c25" stroke-width="1.2"><rect x="3.5" y="1" width="7" height="12" rx="1.2"/><line x1="6" y1="11" x2="8" y2="11"/></svg>
        <span class="contact__bar"></span>
      </li>
      <li class="contact">
        <span>mbellamy@wayfarenow.example</span>
        <svg class="contact__icon" viewBox="0 0 14 14" fill="none" stroke="#ee1c25" stroke-width="1.2"><rect x="1" y="3" width="12" height="8"/><polyline points="1,3 7,8 13,3"/></svg>
        <span class="contact__bar"></span>
      </li>
      <li class="contact">
        <span>www.wayfarenow.example</span>
        <svg class="contact__icon" viewBox="0 0 14 14" fill="none" stroke="#ee1c25" stroke-width="1.2"><circle cx="7" cy="7" r="5.5"/><ellipse cx="7" cy="7" rx="2.4" ry="5.5"/><line x1="1.5" y1="7" x2="12.5" y2="7"/></svg>
        <span class="contact__bar"></span>
      </li>
      <li class="contact">
        <span>4812 Quillmore Ave #164<br>Orlando, FL 32804</span>
        <svg class="contact__icon" viewBox="0 0 14 14" fill="none" stroke="#ee1c25" stroke-width="1.2"><polyline points="1.5,7 7,2 12.5,7"/><polyline points="3,6 3,12 11,12 11,6"/><rect x="6" y="8.5" width="2" height="3.5"/></svg>
        <span class="contact__bar"></span>
      </li>
    </ul>
  </section>

  <section class="card card--back" aria-label="Business card back">
    <span class="brand__dot" aria-hidden="true"></span>
    <span class="brand__name">Wayfare Now</span>
  </section>
</body>
</html>
```